Hollowmere Farm Promotional Leaflet

The team at Hollowmere Farm can help with every aspect of managing and enhancing your home from housekeeping and professional cleaning, laundry and ironing to providing chic and contemporary flower arrangements and even food for your pets!We take pride in providing high-end, consistent and reliable professional services bespoke to you. Whether you are a busy professional working long hours, a stay-at home parent or retired; having professional help in the home gives you time to spend on the things you enjoy.We are providing a very upmarket, highly professional service and need an A5 promotional leaflet to be designed. Please refer to www.hollowmerefarm-example.co.uk and see the section on 'Home Management'The leaflet should incorporate the Hollowmere Farm logo without the 'tipi', and any suitable photography images used on the home page of the website or the 'home management' section.

Target Market(s)

high-end, affluent owners of luxury homes

Industry/Entity Type

Farm

Contact Information for Business Card

The business card design needs to be suitable for use across all of Hollowmere Farm businesses, specifically:
Hollowmere Farm Home Management - otherwise known as Hollowmere Farm @ Home (this uses the typographical logo
Hollowmere Farm Weddings & Events - this uses the 'tipi' logo

Requirements
Must have
• Design in keeping with the look and feel of the logo and website design
• www.hollowmerefarm-example.co.uk

```html
<!DOCTYPE html>
<html lang="en">
<head>
<meta charset="utf-8">
<title>Hollowmere Farm Home Management Leaflet</title>
<link rel="stylesheet" href="https://fonts.googleapis.com/css2?family=Cinzel:wght@400;600;700&family=Lato:wght@400;700&display=swap">
<style>
  :root {
    --pink: #e0268a;
    --pink-deep: #c4147a;
    --gold: #c99a3e;
    --gold-light: #e2b95c;
    --paper: #ffffff;
    --ink: #2b2b2b;
    --stage: #e6e6e6;
  }
  * { box-sizing: border-box; margin: 0; padding: 0; }
  html, body { width: 1200px; height: 1200px; overflow: hidden; background: var(--stage); }
  .leaflet {
    position: absolute; left: 200px; top: 34px; width: 800px; height: 1132px;
    background: var(--paper); overflow: hidden;
    font-family: "Lato", Arial, sans-serif; color: var(--ink);
    box-shadow: 0 8px 30px rgba(0,0,0,.18);
  }
  .leaflet-shapes { position: absolute; inset: 0; }
  .tagline {
    position: absolute; left: 50px; top: 48px; width: 340px;
    font-family: "Cinzel", Georgia, serif; font-size: 19px; line-height: 1.2;
    color: #fff; letter-spacing: .5px;
  }
  .logo-name {
    position: absolute; left: 30px; top: 392px; width: 200px; text-align: center;
    font-family: "Cinzel", Georgia, serif; font-weight: 600; font-size: 24px; line-height: 1.15;
    color: var(--pink);
  }
  .title { position: absolute; left: 44px; top: 572px; font-family: "Cinzel", Georgia, serif; font-weight: 400; }
  .title-main { font-size: 36px; font-weight: 700; color: var(--pink); letter-spacing: 1px; line-height: 1.05; }
  .title-sub { font-size: 29px; font-weight: 600; color: var(--gold); letter-spacing: 1px; line-height: 1.1; margin-top: 4px; }
  .intro {
    position: absolute; left: 36px; top: 672px; width: 440px;
    background: linear-gradient(90deg, var(--pink-deep), var(--pink));
    border: 3px solid var(--gold-light); border-radius: 34px;
    padding: 14px 26px; color: #fff; font-size: 17px; line-height: 1.35;
  }
  .services { position: absolute; left: 40px; top: 792px; list-style: none; }
  .services li { position: relative; padding-left: 30px; font-size: 16px; line-height: 26px; }
  .services li::before {
    content: ""; position: absolute; left: 4px; top: 8px; width: 11px; height: 11px;
    border-radius: 50%; background: var(--gold-light);
  }
  .services li:nth-child(odd)::before { background: var(--pink); }
  .services::before {
    content: ""; position: absolute; left: 9px; top: 12px; bottom: 12px;
    border-left: 2px dashed var(--pink);
  }
  .pitch { position: absolute; left: 520px; top: 515px; width: 250px; color: var(--pink); font-size: 16px; line-height: 1.3; }
  .pitch p + p { margin-top: 16px; }
  .features {
    position: absolute; left: 492px; top: 722px; width: 300px;
    display: grid; grid-template-columns: 1fr 1fr; grid-auto-rows: 100px; column-gap: 6px;
  }
  .feature { text-align: center; font-size: 14px; line-height: 1.2; }
  .feature svg { display: block; margin: 0 auto 5px; }
  .contact { position: absolute; left: 36px; top: 1052px; color: #fff; }
  .contact-call { font-family: "Cinzel", Georgia, serif; font-size: 24px; font-weight: 600; }
  .contact-email { font-size: 15px; margin-top: 8px; }
  .website { position: absolute; right: 28px; bottom: 16px; color: #fff; font-size: 16px; letter-spacing: 1.5px; }
</style>
</head>
<body>
<main class="leaflet">
  <svg class="leaflet-shapes" viewBox="0 0 800 1132" width="800" height="1132" aria-hidden="true">
    <defs>
      <linearGradient id="pinkFill" x1="0" y1="0" x2="1" y2="1">
        <stop offset="0" stop-color="#ea3d9a"/><stop offset="1" stop-color="#c4147a"/>
      </linearGradient>
      <linearGradient id="goldFill" x1="0" y1="0" x2="1" y2="0">
        <stop offset="0" stop-color="#b8872f"/><stop offset=".5" stop-color="#e2b95c"/><stop offset="1" stop-color="#c99a3e"/>
      </linearGradient>
      <linearGradient id="roomTones" x1="0" y1="0" x2="1" y2="1">
        <stop offset="0" stop-color="#d9cfc2"/><stop offset=".5" stop-color="#b38c62"/><stop offset="1" stop-color="#efe9e2"/>
      </linearGradient>
      <linearGradient id="mistFill" x1="0" y1="0" x2="1" y2="1">
        <stop offset="0" stop-color="#ffffff"/><stop offset="1" stop-color="#e4e4e6"/>
      </linearGradient>
    </defs>
    <rect x="0" y="0" width="800" height="600" fill="url(#pinkFill)"/>
    <path d="M0,555 C300,548 560,492 800,436 L800,1132 L0,1132 Z" fill="url(#mistFill)"/>
    <g role="img" aria-label="Faint photo of a relaxed person at home">
      <rect x="300" y="820" width="500" height="200" fill="#e8e8ea" opacity=".6"/>
    </g>
    <path d="M0,545 C300,538 560,482 800,426" fill="none" stroke="url(#goldFill)" stroke-width="18"/>
    <g role="img" aria-label="Photo of a bright open-plan living room with wooden floors and garden doors">
      <path d="M0,330 C220,230 480,165 800,150 L800,400 C560,470 300,512 0,518 Z" fill="url(#roomTones)"/>
    </g>
    <path d="M0,322 C220,222 480,156 800,142" fill="none" stroke="url(#goldFill)" stroke-width="8"/>
    <circle cx="130" cy="420" r="120" fill="#fff"/>
    <circle cx="130" cy="420" r="114" fill="none" stroke="url(#goldFill)" stroke-width="14"/>
    <circle cx="130" cy="420" r="123" fill="none" stroke="#e0268a" stroke-width="3"/>
    <path d="M0,1030 L400,1030 C430,1030 440,1070 480,1070 L800,1070 L800,1132 L0,1132 Z" fill="url(#goldFill)"/>
    <path d="M0,1024 L400,1024 C432,1024 442,1064 480,1064 L800,1064" fill="none" stroke="#e0268a" stroke-width="5"/>
  </svg>

  <p class="tagline">We look after our clients’ homes and holiday lets across South Somerset</p>
  <div class="logo-name">Hollowmere Farm</div>

  <h1 class="title">
    <div class="title-main">HOLLOWMERE FARM</div>
    <div class="title-sub">Home Management</div>
  </h1>

  <p class="intro">The team @ Hollowmere Farm can help with every aspect of managing and enhancing your home including:</p>

  <ul class="services">
    <li>Regular housekeeping and professional cleaning</li>
    <li>Exit cleans</li>
    <li>One-off seasonal /party / building work cleans</li>
    <li>Laundry and ironing</li>
    <li>Chic and contemporary flower arrangements</li>
    <li>Car valeting</li>
    <li>Pet food delivery</li>
    <li>Dry cleaning</li>
  </ul>

  <div class="pitch">
    <p>We take pride in providing high-end, consistent and reliable professional services bespoke to you.</p>
    <p>Coming home to a beautiful environment and being able to relax and enjoy your time is something we all deserve.</p>
  </div>

  <div class="features">
    <div class="feature">
      <svg width="52" height="52" viewBox="0 0 58 58"><circle cx="29" cy="29" r="26" fill="#fff" stroke="#c99a3e" stroke-width="4"/><path d="M18,30 l8,8 l15,-17" fill="none" stroke="#e0268a" stroke-width="4" stroke-linecap="round" stroke-linejoin="round"/></svg>
      Satisfaction guaranteed</div>
    <div class="feature">
      <svg width="52" height="52" viewBox="0 0 58 58"><circle cx="29" cy="29" r="26" fill="#fff" stroke="#c99a3e" stroke-width="4"/><path d="M29,36 C18,28 20,18 26,19 C28,19 29,21 29,22 C29,21 30,19 32,19 C38,18 40,28 29,36 Z" fill="none" stroke="#e0268a" stroke-width="2.5"/><path d="M15,40 h10 l6,3 h12" fill="none" stroke="#e0268a" stroke-width="2.5"/></svg>
      Professional staff you can trust and rely on</div>
    <div class="feature">
      <svg width="52" height="52" viewBox="0 0 58 58"><circle cx="29" cy="29" r="26" fill="#fff" stroke="#c99a3e" stroke-width="4"/><circle cx="29" cy="29" r="14" fill="none" stroke="#e0268a" stroke-width="2.5"/><path d="M23,35 l12,-12" stroke="#e0268a" stroke-width="2.5"/><circle cx="24" cy="24" r="2.5" fill="#e0268a"/><circle cx="34" cy="34" r="2.5" fill="#e0268a"/></svg>
      Competitive rates</div>
    <div class="feature">
      <svg width="52" height="52" viewBox="0 0 58 58"><circle cx="29" cy="29" r="26" fill="#fff" stroke="#c99a3e" stroke-width="4"/><circle cx="29" cy="22" r="6" fill="none" stroke="#e0268a" stroke-width="2.5"/><path d="M18,42 C18,32 40,32 40,42" fill="none" stroke="#e0268a" stroke-width="2.5"/></svg>
      CRB checked and referenced</div>
    <div class="feature">
      <svg width="52" height="52" viewBox="0 0 58 58"><circle cx="29" cy="29" r="26" fill="#fff" stroke="#c99a3e" stroke-width="4"/><rect x="17" y="22" width="24" height="17" rx="2" fill="none" stroke="#e0268a" stroke-width="2.5"/><path d="M24,22 v-4 h10 v4" fill="none" stroke="#e0268a" stroke-width="2.5"/></svg>
      Member of the Domestic Staffing Guild</div>
    <div class="feature">
      <svg width="52" height="52" viewBox="0 0 58 58"><circle cx="29" cy="29" r="26" fill="#fff" stroke="#c99a3e" stroke-width="4"/><path d="M29,14 L41,19 V29 C41,37 35,42 29,44 C23,42 17,37 17,29 V19 Z" fill="none" stroke="#e0268a" stroke-width="2.5"/><path d="M29,23 v12 M23,29 h12" stroke="#e0268a" stroke-width="3"/></svg>
      Fully Insured</div>
  </div>

  <div class="contact">
    <div class="contact-call">CALL US TODAY 07700 900481</div>
    <div class="contact-email">E: info@hollowmerefarm-example.co.uk</div>
  </div>
  <div class="website">visit us-www.hollowmerefarm-example.co.uk</div>
</main>
</body>
</html>
```